Real Estate Marketing Flyer-8.5 by 11 Dual Sided

This is Direct Marketing Flyer targeted to Condo Property owners
to list their condos/townhomes with us. We are looking for Stylish graphics with more upscale design and colors to standout from other agents in the marketplace.

We are open to how it is presented or any design choices made that make flyer standout/appealing.

Target Market(s)

Condo Property Owners..and to lesser extent buyers

Industry/Entity Type

Real Estate

Requirements
Must have
• First Page

Top

Banner with our Team Pic and Names Priscilla, Lou and Bea
(Insert a background photo of condominium complex of upper scale)

"Specializing in Condos/Townhomes"

Buying* Selling* Leasing* Short Sales

1 866 4Suite4 (784-8324)

www.BayviewSuiteGroup.com

When It's time to Sell, Lease of Buy
Contact us for FREE No Obligation Market Consultation

Select Recent Sales By The Bayview Suite Group

7182 W Hollander Ct. # B (688,698)

3 Bedroom 2.5 Bathroom *Represented Buyer*

4217 W Larkfield St. #41
(006,0176)

2 Bedroom 2.5 Bathroom *Water View*

814 S. Marrowbrook-23 2 Bedroom,2.5 Bathroom

3316 W. Loma Tranquila 2 Bedroom 2 Bathroom

26743 Fern Hollow 4 Bedroom 3 Bathrooms

Leasing-We Do That Too

Complete Landlord/Tenant Services

7461 Juniper (54.28)

2 Bedroom, 2 Bathroom

4219 W.Larkfield-38 1 Bedroom, 1 Bathroom

8027 E. Corvallo-216 3 Bedroom, 2.5 Bathroom

937 S. Trellis -D 2 Bedroom 2.5 Bathroom

News You Can Use

Consumer confidence reached a five-year high in May, according to a Merrow Council report also released on Tuesday, with big improvements in Americans’ views about both the current economy and future economic conditions. Consumer spending has also been strikingly resilient so far this year

The Dunmore-Wick 20-city composite index rose 10.9 percent over the last year, the biggest increase since April 2006. Several cities — Charlotte, N.C.; Los Angeles; Portland, Ore.; Seattle; and Tampa, Fla. — had their largest month-over-month gains in more than seven years.

Have you installed Carbon Monoxide detectors in Your Property?

As of July 1, 2011 the Household Air Safety Standards Act (Senate Bill - SB 472) requires owners of all single-family homes with an attached garage or a fossil fuel source to install carbon monoxide detectors within the home by July 1, 2011. Owners of multi-family leased or rental dwellings, such as apartment buildings, have until January 1, 2013 to comply with the law

Home Loan Relief Measure extended through 2013-The BayviewSuiteGroup has extensive experience doing Short Sales-call us for free consultation on doing a No Cost Short Sale.

The best way to cheer yourself up is to try to cheer somebody else up.
Edwin Harlow

Picture of Cute Dog and Cute Bea

We love Pets..When you buy or sell with TheBayviewSuiteGroup-we will make a donation to the animal shelter of your choice.

email contacts

lou@bayviewsuitegroup.com
bea@bayviewsuitegroup.com
priscilla@bayviewsuitegroup.com

(in very small print)

if your property is currently listed with a broker, this is not intention as a solicitation

Nice to have
• We provide cutting edge marketing along with good old fashioned service and hard work

Our "Total Outreach" program offers an overwhelming array of advertising designed to sell your property for top dollar and find the perfect buyer.

We also Provide Free Complete Home Staging consultation, Innovative Value Range Pricing options and so much more.

```html
<!DOCTYPE html>
<html lang="en">
<head>
<meta charset="utf-8">
<title>The Bayview Suite Group – Condo Flyer</title>
<link rel="stylesheet" href="https://fonts.googleapis.com/css2?family=Anton&family=Cinzel:wght@400&family=Raleway:wght@300&family=Gelasio:wght@400&display=swap">
<style>
  :root{
    --lime-top:#8bcf00;
    --olive-bottom:#b2a300;
    --brand-orange:#ff6d00;
    --orange-top:#f39a17;
    --orange-bottom:#ff6a00;
    --charcoal:#333132;
    --badge-green:#9cc93a;
    --ink:#1f1f1f;
    --white:#ffffff;
  }
  *{margin:0;padding:0;box-sizing:border-box}
  html,body{width:927px;height:1200px;overflow:hidden;background:#fff}
  .flyer{position:relative;width:927px;height:1200px;overflow:hidden;font-family:"Gelasio",serif;color:var(--white)}
  .abs{position:absolute}
  h1,h2,h3{font-weight:400}

  .hero{left:0;top:0;width:927px;height:508px;background:linear-gradient(180deg,var(--lime-top) 0%,#9cc000 50%,var(--olive-bottom) 100%)}
  .brand-tab{left:21px;top:0;width:113px;height:146px;background:var(--brand-orange)}
  .team-title{right:48px;top:44px;font-family:"Cinzel",serif;font-size:45px;line-height:1;white-space:nowrap}
  .team-names{right:48px;top:106px;font-family:"Cinzel",serif;font-size:33px;line-height:1;white-space:nowrap}
  .slogan{left:0;width:927px;top:162px;text-align:center;font-family:"Anton",sans-serif;font-size:47px;color:#000;letter-spacing:.5px;
    text-shadow:2px 0 #fff,-2px 0 #fff,0 2px #fff,0 -2px #fff,2px 2px #fff,-2px -2px #fff,2px -2px #fff,-2px 2px #fff;white-space:nowrap}
  .news-label{left:37px;top:258px;font-size:50px;line-height:1}
  .news-body{left:322px;top:258px;width:565px;font-size:16px;line-height:21.7px}
  .news-body p+p{margin-top:21px}

  .photo-back{background:var(--brand-orange)}
  .photo-frame{background:#fff;padding:6px}
  .photo-fill{width:100%;height:100%}
  .condo-back{left:40px;top:322px;width:236px;height:158px;transform:rotate(-4deg)}
  .condo-frame{left:31px;top:318px;width:245px;height:162px;transform:rotate(-4deg)}
  .condo-fill{background:linear-gradient(160deg,#9cc2e8 0%,#d9d6cf 45%,#7f8a6a 100%)}

  .notice{left:0;top:508px;width:927px;height:172px;background:var(--charcoal)}
  .notice h2{position:absolute;left:31px;top:14px;font-size:24px;white-space:nowrap}
  .notice p{position:absolute;left:31px;top:55px;width:875px;font-size:15.2px;line-height:21.8px}

  .promo{left:0;top:680px;width:927px;height:407px;background:linear-gradient(180deg,var(--orange-top) 0%,#f88410 50%,var(--orange-bottom) 100%)}
  .short-sale{left:29px;top:697px;width:890px;font-size:20px;line-height:29px}
  .quote{right:247px;top:772px;text-align:right;color:var(--ink)}
  .quote blockquote{font-size:22px;line-height:29px}
  .quote cite{display:block;font-style:normal;font-size:14.5px;line-height:16px}

  .pets-back{left:44px;top:800px;width:234px;height:154px;transform:rotate(3deg)}
  .pets-frame{left:37px;top:794px;width:240px;height:158px;transform:rotate(3deg)}
  .pets-fill{background:linear-gradient(170deg,#b9d4ee 0%,#c9d1c0 40%,#5fb7d6 70%,#caa06a 100%)}
  .pets-note{left:41px;top:976px;width:270px;font-size:15.5px;line-height:22px}

  .contact-disc{left:364px;top:852px;width:300px;height:300px;border-radius:50%;background:var(--badge-green)}
  .envelope{left:485px;top:876px}
  .contact-heading{left:364px;width:300px;top:912px;text-align:center;font-size:30px;line-height:1.1}
  .contact-list{left:364px;width:300px;top:951px;text-align:center;list-style:none;font-size:16.5px;line-height:27px}
  .hotline{left:399px;top:1040px;font-family:"Anton",sans-serif;font-size:25px;letter-spacing:.3px;white-space:nowrap}

  .team-photo{left:654px;top:839px;width:254px;height:248px;background:linear-gradient(180deg,rgba(40,40,48,0) 0%,#3a3a44 35%,#1e1e26 100%)}

  .footer{left:0;top:1087px;width:927px;height:113px;background:var(--charcoal)}
  .site{left:39px;top:1119px;font-size:21px}
  .disclaimer{left:39px;top:1161px;font-size:10.5px}
  .wordmark{right:44px;top:1136px;font-family:"Raleway",sans-serif;font-weight:300;font-size:25px;letter-spacing:.5px;white-space:nowrap}
</style>
</head>
<body>
<main class="flyer">
  <section class="abs hero"></section>
  <div class="abs brand-tab"></div>
  <h1 class="abs team-title">THE BAYVIEW SUITE GROUP</h1>
  <p class="abs team-names">PRISCILLA, LOU AND BEA</p>
  <p class="abs slogan">"SPECIALIZING IN CONDOS/TOWNHOMES"</p>

  <h2 class="abs news-label">NEWS</h2>
  <div class="abs photo-back condo-back"></div>
  <div class="abs photo-frame condo-frame"><div class="photo-fill condo-fill" role="img" aria-label="Photo of an upscale white townhome with garage and a tree"></div></div>
  <div class="abs news-body">
    <p>Consumer confidence reached a five-year high in May, according to a Merrow Council report also released on Tuesday, with big improvements in Americans’ views about both the current economy and future economic conditions. Consumer spending has also been strikingly resilient so far this year</p>
    <p>The Dunmore-Wick 20-city composite index rose 10.9 percent over the last year, the biggest increase since April 2006. Several cities — Charlotte, N.C.; Los Angeles; Portland, Ore.; Seattle; and Tampa, Fla. — had their largest month-over-month gains in more than seven years.</p>
  </div>

  <section class="abs notice">
    <h2>Have you installed Carbon Monoxide detectors in Your Property?</h2>
    <p>As of July 1, 2011 the Household Air Safety Standards Act (Senate Bill - SB 472) requires owners of all single-family homes with an attached garage or a fossil fuel source to install carbon monoxide detectors within the home by July 1, 2011. Owners of multi-family leased or rental dwellings, such as apartment buildings, have until January 1, 2013 to comply with the law</p>
  </section>

  <section class="abs promo"></section>
  <p class="abs short-sale">Home Loan Relief Measure extended through 2013-The BayviewSuiteGroup has extensive experience doing Short Sales-call us for free consultation on doing a No Cost Short Sale.</p>

  <div class="abs photo-back pets-back"></div>
  <div class="abs photo-frame pets-frame"><div class="photo-fill pets-fill" role="img" aria-label="Photo of a puppy and a kitten beside a community pool"></div></div>
  <p class="abs pets-note">We love Pets..When you buy or sell with TheBayviewSuiteGroup-we will make a donation to the animal shelter of your choice.</p>

  <div class="abs contact-disc"></div>
  <figure class="abs quote">
    <blockquote>The best way to cheer yourself up<br>is to try to cheer somebody else up.</blockquote>
    <cite>Edwin Harlow</cite>
  </figure>
  <svg class="abs envelope" width="58" height="33" viewBox="0 0 58 33" aria-hidden="true">
    <rect x="1.5" y="1.5" width="55" height="30" fill="none" stroke="#1f2a10" stroke-width="3"/>
    <path d="M1.5 1.5 L29 20 L56.5 1.5" fill="none" stroke="#1f2a10" stroke-width="3"/>
  </svg>
  <h3 class="abs contact-heading">email contacts</h3>
  <ul class="abs contact-list">
    <li>lou@bayviewsuitegroup.com</li>
    <li>bea@bayviewsuitegroup.com</li>
    <li>priscilla@bayviewsuitegroup.com</li>
  </ul>
  <p class="abs hotline">1 866 4SUITE4 (784-8324)</p>

  <div class="abs team-photo" role="img" aria-label="Team photo of Priscilla, Lou and Bea in business attire giving thumbs up"></div>

  <footer class="abs footer"></footer>
  <p class="abs site">www.BayviewSuiteGroup.com</p>
  <p class="abs disclaimer">if your property is currently listed with a broker, this is not intention as a solicitation</p>
  <p class="abs wordmark">THE BAYVIEW SUITE GROUP</p>
</main>
</body>
</html>
```